Website for an electrical contractor :)

We are after a web site which can show pictures of our jobs and our capability in a professional, creative and easily understood way.

----- Brightvale Electrical ------

We really want a visually good looking website with three sections

Section one:
'Completed projects'
We have a few pictures of jobs which we've completed and would like to show off with a brief description. (see uploads)

Section two:
'Our capabilities'
Just a list of what services we offer

Section three:
We would like a 'contact us' section which people can send us a short msg and upload a file for plans to be able to send to us. We would need their name, phone number and email details. We would also need a short privacy policy saying 'we do not disclose information to third parties'.
We also want to display our contact number and postal address

Good luck :)

Target Market(s)

Adults 25 years+
Business owners
Builders
Real estate agents

Industry/Entity Type

Electrical

Colors

Designer to choose colors to be used in the design.

Requirements
Must have
• Visually appealing
Easy to understand
In the 'Completed projects' section, must have a list for each project we do i can upload pictures for it.

```html
<!DOCTYPE html>
<html lang="en">
<head>
<meta charset="utf-8">
<title>Brightvale Electrical &amp; Communications</title>
<link rel="stylesheet" href="https://fonts.googleapis.com/css2?family=Lato:ital,wght@0,400;0,700;1,400&family=Playfair+Display:ital,wght@1,700&family=Raleway:wght@300;400&display=swap">
<style>
:root{
  --ink:#333;
  --muted:#666;
  --red:#d9262c;
  --nav:#575757;
  --service-bg:#5b5b5b;
  --contact-bg:#1f1f1f;
  --white:#fff;
  --line:#e2e2e2;
}
*{box-sizing:border-box;margin:0;padding:0}
html,body{width:1200px;height:3002px;overflow:hidden}
body{position:relative;font-family:"Lato",sans-serif;color:var(--ink);background:var(--white)}
.abs{position:absolute}

/* header */
.site-header{left:0;top:0;width:1200px;height:148px;background:linear-gradient(#fafafa,#efefef)}
.brand{left:125px;top:40px;display:flex;align-items:center;gap:14px}
.brand-dot{width:34px;height:34px;border-radius:50%;background:var(--red)}
.brand-name{font-family:"Lato",sans-serif;font-weight:400;font-size:50px;color:#555;line-height:1}
.header-contact{left:800px;top:14px;font-size:14px;color:var(--muted);line-height:1.35}
.header-contact .row{display:flex;align-items:center;gap:10px;margin-bottom:14px}
.header-contact .row.tight{margin-bottom:0}
.hc-icon{width:14px;height:14px;fill:var(--red);flex:none}
.header-contact .pair{display:flex;gap:32px}
.header-contact .pair span{display:flex;align-items:center;gap:10px}

/* nav */
.main-nav{left:0;top:148px;width:1200px;height:70px;background:var(--nav)}
.main-nav ul{list-style:none}
.main-nav li{position:absolute;top:0;height:70px;line-height:70px;font-size:13px;color:var(--white);letter-spacing:.3px}
.main-nav li.active{background:var(--white);color:var(--ink);text-align:center}
.search{left:913px;top:20px;width:162px;height:32px;background:var(--white);font-size:11px;color:#555;padding:0 8px;line-height:32px}
.search svg{position:absolute;right:8px;top:7px;width:18px;height:18px;stroke:#333;fill:none;stroke-width:2}

/* hero */
.hero{left:0;top:218px;width:1200px;height:545px;background:linear-gradient(180deg,#4e5a6c 0%,#6d7686 35%,#4a4a4c 65%,#3a3a3a 100%)}
.hero-title{left:123px;top:160px;font-family:"Raleway",sans-serif;font-weight:300;font-size:76px;color:var(--white);letter-spacing:1px}
.hero-sub{left:123px;top:256px;font-family:"Raleway",sans-serif;font-weight:400;font-size:30px;color:var(--white)}
.btn{display:flex;align-items:center;justify-content:center;gap:8px;border-radius:20px;font-size:12px;font-weight:700;letter-spacing:.3px}
.btn-light{left:123px;top:319px;width:138px;height:39px;background:var(--white);color:var(--ink)}
.btn-dark{background:#3b3b3b;color:var(--white);box-shadow:0 2px 0 #222}
.btn svg{width:12px;height:12px}
.slide-arrow{top:251px;width:40px;height:40px;border-radius:50%;background:var(--white);display:flex;align-items:center;justify-content:center}
.slide-arrow svg{width:14px;height:14px;stroke:#333;stroke-width:3;fill:none}

/* about */
.about-media{left:125px;top:804px;width:461px;height:319px;background:linear-gradient(160deg,#2b2b2b 0%,#a38b6c 45%,#e8e2d8 75%,#cfcfcf 100%);border-radius:6px}
.section-title{font-family:"Playfair Display",serif;font-style:italic;font-weight:700;font-size:34px}
.about-title{left:616px;top:812px;color:#222}
.about-copy{left:614px;top:880px;width:462px;font-size:11px;font-style:italic;color:#444;line-height:1.6}
.about-copy p{margin-bottom:17px}
.about-btn{left:614px;top:1137px;width:138px;height:39px}

/* services */
.services{left:0;top:1224px;width:1200px;height:431px;background:var(--service-bg)}
.services-title{left:125px;top:40px;color:var(--white)}
.tabs{left:125px;top:99px;width:950px;height:55px;border:2px solid var(--white)}
.tab{position:absolute;top:7px;height:37px;width:452px;background:var(--white);font-size:16px;font-style:italic;color:#555;text-align:center;line-height:37px}
.service-col{top:180px;list-style:none;color:var(--white);font-size:12.5px;font-style:italic;line-height:19.8px}
.service-col li{display:flex;align-items:center;gap:9px}
.service-col li svg{width:11px;height:11px;flex:none}

/* projects */
.projects-title{left:125px;top:1686px;color:#222}
.project{width:218px;height:218px;border-radius:50%;border:2px solid #333}
.project-tools{display:flex;gap:8px;left:66px;top:90px}
.tool{width:34px;height:34px;border-radius:4px;display:flex;align-items:center;justify-content:center}
.tool svg{width:18px;height:18px;stroke:#fff;fill:none;stroke-width:2}
.dots{left:578px;top:2246px;display:flex;gap:4px}
.dots span{width:12px;height:12px;border-radius:50%;background:#444}
.dots span.on{background:var(--white);border:1.5px solid #444}

/* contact */
.contact{left:0;top:2302px;width:1200px;height:700px;background:var(--contact-bg);color:var(--white)}
.contact-title{left:125px;top:26px}
.c-icon{width:54px;height:54px;border-radius:50%;border:2px solid var(--white);display:flex;align-items:center;justify-content:center;top:87px}
.c-icon svg{width:22px;height:22px;fill:var(--white)}
.c-text{top:160px;font-size:13px;text-align:center;line-height:1.5;width:250px}
.newsletter{left:858px;top:162px;width:217px;height:34px;background:var(--white);color:#555;font-size:10px;line-height:34px;padding-left:10px}
.newsletter .go{position:absolute;right:5px;top:4px;width:36px;height:26px;background:#222;display:flex;align-items:center;justify-content:center}
.newsletter .go svg{width:16px;height:16px;fill:var(--white)}
.field{background:var(--white);color:#555;font-size:10px;padding:0 10px;line-height:39px;height:39px;top:253px}
.field-message{left:125px;top:300px;width:950px;height:93px;line-height:1;padding-top:12px}
.send{left:531px;top:411px;width:136px;height:39px;border-radius:20px;background:var(--white);color:#333;font-size:16px;display:flex;align-items:center;justify-content:center;letter-spacing:1px}
.social{top:485px;width:54px;height:54px;border-radius:50%;border:2px solid var(--white)}
.footer-rule{left:125px;top:587px;width:950px;height:1px;background:#444}
.copyright{left:0;top:634px;width:1200px;text-align:center;font-size:10px;font-style:italic;color:#aaa}
</style>
</head>
<body>

<header class="site-header abs">
  <div class="brand abs">
    <span class="brand-dot"></span>
    <span class="brand-name">Brightvale</span>
  </div>
  <div class="header-contact abs">
    <div class="row pair">
      <span><svg class="hc-icon" viewBox="0 0 16 16"><rect width="16" height="16" rx="3"/></svg>0400 555 218</span>
      <span><svg class="hc-icon" viewBox="0 0 16 16"><rect width="16" height="16" rx="3"/></svg>08 9000 3141</span>
    </div>
    <div class="row"><svg class="hc-icon" viewBox="0 0 16 16"><path d="M1 3h14v10H1z M1 3l7 6 7-6" stroke="#d9262c" fill="none" stroke-width="1.6"/></svg>info@brightvaleelectrical.com.au</div>
    <div class="row tight"><svg class="hc-icon" viewBox="0 0 16 16"><path d="M8 0a5.5 5.5 0 0 0-5.5 5.5C2.5 10 8 16 8 16s5.5-6 5.5-10.5A5.5 5.5 0 0 0 8 0zm0 8a2.5 2.5 0 1 1 0-5 2.5 2.5 0 0 1 0 5z"/></svg><span>P.O Box 140 Northgate W.A 6000<br>A.B.N: 12 345 678 901</span></div>
  </div>
</header>

<nav class="main-nav abs">
  <ul>
    <li class="active" style="left:125px;width:65px">HOME</li>
    <li style="left:234px">ABOUT US</li>
    <li style="left:356px">OUR SERVICES</li>
    <li style="left:509px">OUR PROJECT</li>
    <li style="left:657px">BLOG</li>
    <li style="left:750px">CONTACT US</li>
  </ul>
  <div class="search abs">Search<svg viewBox="0 0 20 20"><circle cx="8" cy="8" r="6"/><path d="M12.5 12.5L18 18"/></svg></div>
</nav>

<section class="hero abs" role="img" aria-label="Modern commercial building with brick and glass facade under a cloudy sky">
  <h1 class="hero-title abs">Wel come To...!!!</h1>
  <p class="hero-sub abs">Brightvale Electrical &amp; Communication</p>
  <div class="btn btn-light abs">LEARN MORE <svg viewBox="0 0 12 12"><circle cx="6" cy="6" r="6" fill="#333"/><path d="M5 3.5L7.5 6 5 8.5" stroke="#fff" stroke-width="1.5" fill="none"/></svg></div>
  <div class="slide-arrow abs" style="left:16px"><svg viewBox="0 0 14 14"><path d="M9 2L4 7l5 5"/></svg></div>
  <div class="slide-arrow abs" style="left:1141px"><svg viewBox="0 0 14 14"><path d="M5 2l5 5-5 5"/></svg></div>
</section>

<section class="about">
  <div class="about-media abs" role="img" aria-label="Desktop monitor showing a company site sign at a construction site"></div>
  <h2 class="section-title about-title abs">About Us...</h2>
  <div class="about-copy abs">
    <p>Lorem ipsum dolor sit amet, consectetur adipiscing elit. Integer commodo tristique odio, quis fringilla ligula aliquet utpisci.We can do very cool stuff with paper &amp; scissors. This is a place-holder text for this service. It's just to give you an idea of how the stuff will look like.Some people use well thought strategies. We just drop bombs.</p>
    <p>Just kidding. Our strategy works and your amount of sales will explode someday.f stock images don't seem to do the job, why not use authentic ones? We'll make sure every pixel will look crisp and at its best.</p>
    <p>Lorem ipsum dolor sit amet, consectetur adipiscing elit. Integer commodo tristique odio, quis fringilla ligula aliquet utpisci.We can do very cool stuff with paper &amp; scissors. This is a place-holder text for this service.</p>
  </div>
  <div class="btn btn-dark about-btn abs">LEARN MORE <svg viewBox="0 0 12 12"><circle cx="6" cy="6" r="6" fill="#fff"/><path d="M5 3.5L7.5 6 5 8.5" stroke="#333" stroke-width="1.5" fill="none"/></svg></div>
</section>

<svg width="0" height="0" style="position:absolute">
  <defs>
    <symbol id="bullet" viewBox="0 0 12 12"><circle cx="6" cy="6" r="6" fill="#fff"/><path d="M5 3.5L7.5 6 5 8.5" stroke="#333" stroke-width="1.6" fill="none"/></symbol>
  </defs>
</svg>

<section class="services abs">
  <h2 class="section-title services-title abs">Our Service...</h2>
  <div class="tabs abs">
    <div class="tab" style="left:6px">Residential</div>
    <div class="tab" style="left:484px">Commercial / Industrial</div>
  </div>
  <ul class="service-col abs" style="left:125px">
    <li><svg><use href="#bullet"/></svg>24hr Support / faults</li>
    <li><svg><use href="#bullet"/></svg>RCD (Safety Switch) installations</li>
    <li><svg><use href="#bullet"/></svg>Smoke alarms</li>
    <li><svg><use href="#bullet"/></svg>Power points</li>
    <li><svg><use href="#bullet"/></svg>Lighting points</li>
    <li><svg><use href="#bullet"/></svg>External lighting</li>
    <li><svg><use href="#bullet"/></svg>Sensor lighting</li>
    <li><svg><use href="#bullet"/></svg>Switching</li>
    <li><svg><use href="#bullet"/></svg>Antennas and Arial points</li>
    <li><svg><use href="#bullet"/></svg>Dimmers</li>
    <li><svg><use href="#bullet"/></svg>Ceiling fans</li>
  </ul>
  <ul class="service-col abs" style="left:370px">
    <li><svg><use href="#bullet"/></svg>Exhaust fans</li>
    <li><svg><use href="#bullet"/></svg>Kitchen / Bathroom Projects</li>
    <li><svg><use href="#bullet"/></svg>Re-wires</li>
    <li><svg><use href="#bullet"/></svg>Smart wiring</li>
    <li><svg><use href="#bullet"/></svg>Phone points</li>
    <li><svg><use href="#bullet"/></svg>Data points</li>
    <li><svg><use href="#bullet"/></svg>Mains/sub mains cabling</li>
    <li><svg><use href="#bullet"/></svg>Switchboard installations</li>
    <li><svg><use href="#bullet"/></svg>Compliance investigations</li>
    <li><svg><use href="#bullet"/></svg>Concrete and wall chasing</li>
    <li><svg><use href="#bullet"/></svg>Temporary builders site power</li>
  </ul>
  <ul class="service-col abs" style="left:612px">
    <li><svg><use href="#bullet"/></svg>24hr Support / faults</li>
    <li><svg><use href="#bullet"/></svg>Lighting/power design</li>
    <li><svg><use href="#bullet"/></svg>Commercial lighting</li>
    <li><svg><use href="#bullet"/></svg>Emergency and exit lighting</li>
    <li><svg><use href="#bullet"/></svg>Led strip lighting</li>
    <li><svg><use href="#bullet"/></svg>Energy efficient lighting</li>
    <li><svg><use href="#bullet"/></svg>Temporary lighting</li>
    <li><svg><use href="#bullet"/></svg>Illuminated signage</li>
    <li><svg><use href="#bullet"/></svg>Switchboard relocations</li>
    <li><svg><use href="#bullet"/></svg>Maintenance</li>
  </ul>
  <ul class="service-col abs" style="left:858px">
    <li><svg><use href="#bullet"/></svg>RCD installation</li>
    <li><svg><use href="#bullet"/></svg>Phone/data points</li>
    <li><svg><use href="#bullet"/></svg>Data cabinets</li>
    <li><svg><use href="#bullet"/></svg>Data Networking</li>
    <li><svg><use href="#bullet"/></svg>IDF installations/relocations</li>
    <li><svg><use href="#bullet"/></svg>All power requirements</li>
    <li><svg><use href="#bullet"/></svg>All three phase power require ments</li>
    <li><svg><use href="#bullet"/></svg>Electrical rip outs / Disconnections</li>
    <li><svg><use href="#bullet"/></svg>Thermal Imaging scans</li>
    <li><svg><use href="#bullet"/></svg>Concrete and wall chasing</li>
  </ul>
</section>

<section class="projects">
  <h2 class="section-title projects-title abs">Our Projects...</h2>
  <div class="project abs" style="left:125px;top:1753px;background:radial-gradient(circle,#5a4f48,#2a2522)" role="img" aria-label="Company site sign at a completed project, shown with hover overlay">
    <div class="project-tools abs">
      <div class="tool" style="background:var(--red)"><svg viewBox="0 0 18 18"><path d="M7 11l4-4M6 8l-2 2a2.5 2.5 0 0 0 4 4l2-2M12 10l2-2a2.5 2.5 0 0 0-4-4L8 6"/></svg></div>
      <div class="tool" style="background:#444"><svg viewBox="0 0 18 18"><circle cx="8" cy="8" r="5"/><path d="M12 12l4 4"/></svg></div>
    </div>
  </div>
  <div class="project abs" style="left:368px;top:1753px;background:radial-gradient(circle at 50% 40%,#d9d6cf,#8a847b)" role="img" aria-label="Open-plan interior hall with new downlights"></div>
  <div class="project abs" style="left:612px;top:1753px;background:radial-gradient(circle at 50% 40%,#ece8e2,#a59d92)" role="img" aria-label="Furnished lounge area with ceiling lighting"></div>
  <div class="project abs" style="left:857px;top:1753px;background:linear-gradient(180deg,#4f86c6 0%,#8db3dc 45%,#6b5a4e 60%,#9a8f83 100%)" role="img" aria-label="Newly built brick house under blue sky"></div>
  <div class="project abs" style="left:125px;top:2000px;background:linear-gradient(180deg,#5b8fcc 0%,#a0c1e2 45%,#7a4e3a 62%,#c9b49a 100%)" role="img" aria-label="Brick home with sandy front yard under construction"></div>
  <div class="project abs" style="left:368px;top:2000px;background:linear-gradient(180deg,#cfcfcf 0%,#eeeeee 40%,#5c5c5c 75%,#3c3c3c 100%)" role="img" aria-label="Commercial office fit-out with ceiling panels and windows"></div>
  <div class="project abs" style="left:612px;top:2000px;background:linear-gradient(180deg,#3e3e3e 0%,#6e6e6e 50%,#8d8b86 100%)" role="img" aria-label="Steel roof framing of a warehouse under construction"></div>
  <div class="project abs" style="left:857px;top:2000px;background:linear-gradient(180deg,#8c6f5a 0%,#5a4537 60%,#3b2e25 100%)" role="img" aria-label="Reinforcement mesh and conduit laid before a concrete pour"></div>
  <div class="dots abs"><span class="on"></span><span></span><span></span></div>
</section>

<section class="contact abs">
  <h2 class="section-title contact-title abs">Contact Us...</h2>

  <div class="c-icon abs" style="left:205px"><svg viewBox="0 0 24 24"><rect x="3" y="3" width="18" height="18" rx="3"/><path d="M9 7c-1 0-2 1-1.6 2.4.8 3 3.2 5.4 6.2 6.2C15 16 16 15 16 14l-2-1.2-1 1c-1.5-.7-2.6-1.8-3.3-3.3l1-1z" fill="#1f1f1f"/></svg></div>
  <div class="c-icon abs" style="left:448px"><svg viewBox="0 0 24 24"><path d="M3 6h18v12H3z M3 6l9 7 9-7" fill="none" stroke="#fff" stroke-width="2"/></svg></div>
  <div class="c-icon abs" style="left:692px"><svg viewBox="0 0 24 24"><path d="M12 2a7 7 0 0 0-7 7c0 5.5 7 13 7 13s7-7.5 7-13a7 7 0 0 0-7-7zm0 10a3 3 0 1 1 0-6 3 3 0 0 1 0 6z"/></svg></div>
  <div class="c-icon abs" style="left:939px"><svg viewBox="0 0 24 24"><path d="M3 9h18v11H3z M3 9l9-6 9 6 M8 20v-6h8v6" fill="none" stroke="#fff" stroke-width="2"/></svg></div>

  <p class="c-text abs" style="left:107px">0400 555 218 &nbsp;/&nbsp; 08 9000 3141</p>
  <p class="c-text abs" style="left:350px">info@brightvaleelectrical.com.au</p>
  <p class="c-text abs" style="left:594px">P.O Box 140 Northgate W.A 6000<br>A.B.N: 12 345 678 901</p>
  <div class="newsletter abs">Enter Your Email Address<span class="go"><svg viewBox="0 0 16 16"><path d="M1 8l14-6-5 13-2-5z"/></svg></span></div>

  <div class="field abs" style="left:125px;width:299px">Name :</div>
  <div class="field abs" style="left:450px;width:299px">Phone :</div>
  <div class="field abs" style="left:778px;width:297px">Email Address :</div>
  <div class="field field-message abs">Message :</div>
  <div class="send abs">SEND</div>

  <div class="social abs" style="left:409px"></div>
  <div class="social abs" style="left:490px"></div>
  <div class="social abs" style="left:571px"></div>
  <div class="social abs" style="left:652px"></div>
  <div class="social abs" style="left:733px"></div>

  <div class="footer-rule abs"></div>
  <p class="copyright abs">© Copy Right 2013-2015 Brightvale Electrical . &nbsp;| &nbsp;Privacy Policy &nbsp;| &nbsp;All rights reserved.</p>
</section>

</body>
</html>
```